Tequila Bottle Labels

We are a construction company that bottled our own tequila and would like a unique label for it! We already have our own company logo (linked below) and we want that logo somewhere on the bottle as well- it can be big or small. It was brewed & bottled in Southern California. Ideally it would have the year "2020," "Single Estate," & "100% Agave Azul" somewhere on the label.

Tequila / RMT / 2020

```html
<!DOCTYPE html>
<html lang="en">
<head>
<meta charset="utf-8">
<title>Tequila Labels – RMT 2020</title>
<link href="https://fonts.googleapis.com/css2?family=Rye&family=Josefin+Sans:wght@400;600&family=Libre+Baskerville:wght@700&display=swap" rel="stylesheet">
<style>
  :root {
    --navy: #1d4583;
    --green: #8cc63f;
    --paper: #ffffff;
    --ink: #333a44;
    --bg-light: #f2f2f2;
    --bg-dark: #cfcfcf;
  }
  * { box-sizing: border-box; margin: 0; padding: 0; }
  html, body { width: 1200px; height: 998px; overflow: hidden; }
  body {
    position: relative;
    background: radial-gradient(ellipse at 50% 30%, var(--bg-light) 0%, #e3e3e3 55%, var(--bg-dark) 100%);
    font-family: "Josefin Sans", sans-serif;
    color: var(--ink);
  }
  .label {
    position: absolute;
    background: var(--paper);
    overflow: hidden;
    box-shadow: 0 2px 6px rgba(0,0,0,.12);
  }
  .label--tall { left: 100px; top: 254px; width: 400px; height: 490px; }
  .label--wide { left: 550px; top: 299px; width: 560px; height: 400px; }

  .edge { position: absolute; left: 0; width: 100%; height: 16px; }
  .edge--top { top: 0; background: var(--navy); }
  .edge--bottom { bottom: 0; background: var(--green); }

  .stripe { position: absolute; left: 0; width: 100%; height: 14px; transform: translateY(-50%); }
  .stripe--green { background: var(--green); }
  .stripe--navy { background: var(--navy); }

  .emblem { position: absolute; left: 50%; width: 106px; height: 106px; transform: translate(-50%, -50%); }
  .emblem__text { font-family: "Josefin Sans", sans-serif; font-size: 7.4px; font-weight: 600; letter-spacing: 1px; fill: var(--ink); text-transform: uppercase; }

  .title {
    position: absolute; left: 0; width: 100%; text-align: center;
    font-family: "Rye", serif; color: var(--navy); letter-spacing: 2px;
    text-shadow: 2px 2px 0 #d9dde3;
  }
  .year {
    position: absolute; left: 50%; transform: translateX(-50%);
    width: 64px; text-align: center;
    font-size: 11px; letter-spacing: 6px; padding: 5px 0 4px 6px;
    border-top: 1px solid var(--navy); border-bottom: 1px solid var(--navy);
    color: var(--ink);
  }
  .brand {
    position: absolute; left: 50%; width: 56px; height: 56px;
    transform: translate(-50%, -50%);
    border-radius: 50%; background: var(--paper); border: 1px solid #b9c3d3;
    display: flex; align-items: center; justify-content: center;
    font-family: "Libre Baskerville", serif; font-weight: 700; font-size: 17px;
    color: var(--navy); letter-spacing: -0.5px;
  }
  .detail {
    position: absolute; font-size: 8.5px; font-weight: 600;
    font-variant: small-caps; letter-spacing: .6px; text-align: center;
    font-size: 10px; color: var(--ink);
  }
  .detail--rule { border-top: 1px solid var(--navy); border-bottom: 1px solid var(--navy); padding: 4px 4px 2px; }

  /* tall label positions */
  .label--tall .stripe--green, .label--tall .emblem { top: 25%; }
  .label--tall .title { top: 150px; font-size: 60px; }
  .label--tall .year { top: 260px; }
  .label--tall .stripe--navy, .label--tall .brand { top: 340px; }
  .label--tall .detail--estate { left: 0; width: 100%; top: 382px; }
  .label--tall .detail--agave { left: 50%; transform: translateX(-50%); top: 406px; }

  /* wide label positions */
  .label--wide .stripe--green, .label--wide .emblem { top: 22%; }
  .label--wide .title { top: 125px; font-size: 64px; }
  .label--wide .year { top: 232px; }
  .label--wide .stripe--navy, .label--wide .brand { top: 306px; }
  .label--wide .detail--estate { left: 135px; top: 340px; }
  .label--wide .detail--agave { right: 125px; top: 340px; }
</style>
</head>
<body>

<section class="label label--tall" aria-label="Tequila label, tall format">
  <div class="edge edge--top" role="img" aria-label="Navy zigzag border"></div>
  <div class="stripe stripe--green"></div>
  <svg class="emblem" viewBox="0 0 100 100" aria-label="Brewed and bottled in Southern California seal">
    <defs>
      <path id="arcTopA" d="M14,50 A36,36 0 0 1 86,50"/>
      <path id="arcBotA" d="M10,50 A40,40 0 0 0 90,50"/>
    </defs>
    <circle cx="50" cy="50" r="46" fill="#fff"/>
    <circle cx="50" cy="50" r="27" fill="var(--green)" role="img" aria-label="Agave plant illustration"/>
    <text class="emblem__text"><textPath href="#arcTopA" startOffset="50%" text-anchor="middle">Brewed &amp; Bottled in</textPath></text>
    <text class="emblem__text"><textPath href="#arcBotA" startOffset="50%" text-anchor="middle">Southern California</textPath></text>
  </svg>
  <h1 class="title">TEQUILA</h1>
  <div class="year">2020</div>
  <div class="stripe stripe--navy"></div>
  <div class="brand">RMT</div>
  <p class="detail detail--estate">Single Estate</p>
  <p class="detail detail--agave detail--rule">100% Agave Azul</p>
  <div class="edge edge--bottom" role="img" aria-label="Green zigzag border"></div>
</section>

<section class="label label--wide" aria-label="Tequila label, wide format">
  <div class="edge edge--top" role="img" aria-label="Navy zigzag border"></div>
  <div class="stripe stripe--green"></div>
  <svg class="emblem" viewBox="0 0 100 100" aria-label="Brewed and bottled in Southern California seal">
    <defs>
      <path id="arcTopB" d="M14,50 A36,36 0 0 1 86,50"/>
      <path id="arcBotB" d="M10,50 A40,40 0 0 0 90,50"/>
    </defs>
    <circle cx="50" cy="50" r="46" fill="#fff"/>
    <circle cx="50" cy="50" r="27" fill="var(--green)" role="img" aria-label="Agave plant illustration"/>
    <text class="emblem__text"><textPath href="#arcTopB" startOffset="50%" text-anchor="middle">Brewed &amp; Bottled in</textPath></text>
    <text class="emblem__text"><textPath href="#arcBotB" startOffset="50%" text-anchor="middle">Southern California</textPath></text>
  </svg>
  <h1 class="title">TEQUILA</h1>
  <div class="year">2020</div>
  <div class="stripe stripe--navy"></div>
  <div class="brand">RMT</div>
  <p class="detail detail--estate detail--rule">Single Estate</p>
  <p class="detail detail--agave detail--rule">100% Agave Azul</p>
  <div class="edge edge--bottom" role="img" aria-label="Green zigzag border"></div>
</section>

</body>
</html>
```